Luxury Bath Flyer

I would like to have a professional Flyer, which would describe a beautiful atmospheric luxury-Bath situation. I am sending you a( screenshot) Flyer Proposal, which shoes my intention and wish how I would like to have it. Please note that Ästhetik and a professional Flyer is very important to me. If possible send a psd.file or a indesign file, in case of we gonna need to change the text. You are also free to make 2 different proposals and one as you would suggest.?(I send you couple pictures, but the main one which I choose on the pdf file, please keep that, it is called " KR-71" - If there is a question please let me know. Looking forward to receive an amazing artwork.Kind Regards Merle
Look and feel
Each slider illustrates characteristics of the customer's brand and the style your logo design should communicate.

```html
<!DOCTYPE html>
<html lang="de">
<head>
<meta charset="utf-8">
<title>Wohnquell – Bad Flyer</title>
<link href="https://fonts.googleapis.com/css2?family=Oswald:wght@500;600;700&family=Open+Sans:wght@400;600&display=swap" rel="stylesheet">
<style>
  :root{
    --stage:#cbcbcb;
    --orange:#f26722;
    --orange-light:#f7941d;
    --blue:#0d5aa7;
    --blue-light:#1c8fd6;
    --dark:#3a3a3c;
    --ink:#222;
    --white:#fff;
  }
  html,body{margin:0;padding:0;width:1200px;height:1200px;overflow:hidden;background:var(--stage);}
  .flyer{position:absolute;left:220px;top:68px;width:761px;height:1065px;background:var(--white);overflow:hidden;font-family:"Open Sans",sans-serif;}
  .top-band{position:absolute;left:0;top:0;width:761px;height:90px;background:linear-gradient(90deg,var(--orange-light) 40%,var(--orange));}
  .top-band::after{content:"";position:absolute;left:0;bottom:-4px;width:100%;height:4px;background:var(--white);}
  .top-band .edge{position:absolute;left:0;top:0;width:38px;height:90px;background:var(--orange);}
  .address{position:absolute;left:528px;top:36px;display:flex;align-items:center;gap:12px;color:var(--white);font-weight:600;font-size:13px;line-height:18px;}
  .hero{position:absolute;left:0;top:96px;width:761px;height:549px;background:linear-gradient(160deg,#d9d2c8 0%,#c7beb2 40%,#8a6f58 72%,#5b4636 100%);}
  .brand-tab{position:absolute;left:44px;top:0;width:246px;height:188px;z-index:2;filter:drop-shadow(0 2px 4px rgba(0,0,0,.25));}
  .brand-tab .tab-shape{position:absolute;left:0;top:0;}
  .brand-name{position:absolute;left:0;top:62px;width:246px;text-align:center;font-family:"Open Sans",sans-serif;font-weight:600;font-size:34px;color:var(--ink);}
  .headline{position:absolute;left:29px;top:668px;font-family:"Oswald",sans-serif;font-weight:600;text-transform:uppercase;line-height:1;white-space:nowrap;}
  .headline .kicker{color:var(--orange);font-size:29px;letter-spacing:-.4px;}
  .headline .main{color:var(--blue);font-size:41px;margin-top:9px;letter-spacing:-.5px;}
  .headline .sub{color:var(--blue);font-size:29px;margin-top:7px;letter-spacing:-.4px;}
  .pill{position:absolute;font-family:"Oswald",sans-serif;font-weight:600;color:var(--white);text-transform:uppercase;background:var(--orange);}
  .services-pill{left:0;top:816px;width:264px;height:35px;border-radius:0 18px 18px 0;font-size:26px;line-height:35px;padding-left:29px;box-sizing:border-box;}
  .services{position:absolute;left:50px;top:868px;margin:0;padding:0;list-style:none;font-size:13.5px;color:var(--ink);}
  .services li{display:flex;align-items:center;gap:7px;height:29.6px;}
  .benefits-panel{position:absolute;left:478px;top:645px;width:256px;height:350px;background:var(--dark);}
  .detail-photo{position:absolute;left:489px;top:522px;width:236px;height:236px;border-radius:50%;border:4px solid var(--white);box-sizing:border-box;background:linear-gradient(170deg,#c9a98c 0%,#d8c3ad 45%,#f4f2ef 70%,#e8e4df 100%);z-index:3;box-shadow:0 2px 6px rgba(0,0,0,.3);}
  .benefits-pill{left:494px;top:778px;width:212px;height:37px;border-radius:19px;font-size:27px;line-height:37px;text-align:center;}
  .benefits{position:absolute;left:498px;top:840px;margin:0;padding:0;list-style:none;color:var(--white);font-size:13.5px;}
  .benefits li{display:flex;align-items:center;gap:14px;height:52px;}
  .footer{position:absolute;left:0;top:1000px;width:761px;height:65px;}
  .footer .footer-bg{position:absolute;left:0;top:0;}
  .contact{position:absolute;top:22px;display:flex;align-items:center;gap:14px;color:var(--white);font-size:13.5px;}
  .contact svg{flex:none;}
  .contact.web{left:42px;}
  .contact.mail{left:267px;}
  .divider{position:absolute;left:226px;top:21px;width:2px;height:24px;background:var(--orange);}
  .phone{position:absolute;left:500px;top:10px;display:flex;align-items:center;gap:10px;color:var(--white);font-family:"Oswald",sans-serif;font-weight:600;font-size:34px;line-height:44px;}
  .phone svg{flex:none;}
</style>
</head>
<body>
<div class="flyer">
  <div class="hero" role="img" aria-label="Fotografie eines modernen Badezimmers mit Holz-Waschtisch, Mosaikfliesen und freistehender Badewanne"></div>

  <div class="top-band">
    <div class="edge"></div>
    <div class="address">
      <svg width="30" height="32" viewBox="0 0 30 32" fill="none" stroke="#fff" stroke-width="2.4"><path d="M15 3a7 7 0 0 1 7 7c0 6-7 12-7 12s-7-6-7-12a7 7 0 0 1 7-7z" fill="#fff"/><circle cx="15" cy="10" r="2.6" fill="#f7941d" stroke="none"/><path d="M8 22c-4 1-5 2.5-5 3.5 0 2 5 3.5 12 3.5s12-1.5 12-3.5c0-1-1-2.5-5-3.5"/></svg>
      <span>Lindenweg 14,<br>4020 Talheim</span>
    </div>
  </div>

  <div class="brand-tab">
    <svg class="tab-shape" width="246" height="188" viewBox="0 0 246 188"><path d="M0 0H246V158L123 188L0 158Z" fill="#fff"/></svg>
    <div class="brand-name">Wohnquell</div>
  </div>

  <div class="benefits-panel"></div>
  <div class="detail-photo" role="img" aria-label="Detailfoto eines Aufsatzwaschbeckens mit Armatur vor Mosaikfliesen und Tulpen"></div>

  <div class="headline">
    <div class="kicker">Ihr exklusives Bad zum Fixpreis!</div>
    <div class="main">Wir montieren für Sie...</div>
    <div class="sub">Und das „Alles aus einer Hand“!</div>
  </div>

  <div class="pill services-pill">Unsere Services</div>
  <ul class="services">
    <li><svg width="12" height="12" viewBox="0 0 12 12"><circle cx="6" cy="6" r="6" fill="#f26722"/><path d="M3.2 6.2l2 2 3.6-4" stroke="#fff" stroke-width="1.6" fill="none"/></svg>Markenbäder zum Online Preis</li>
    <li><svg width="12" height="12" viewBox="0 0 12 12"><circle cx="6" cy="6" r="6" fill="#f26722"/><path d="M3.2 6.2l2 2 3.6-4" stroke="#fff" stroke-width="1.6" fill="none"/></svg>Wir montieren für Sie</li>
    <li><svg width="12" height="12" viewBox="0 0 12 12"><circle cx="6" cy="6" r="6" fill="#f26722"/><path d="M3.2 6.2l2 2 3.6-4" stroke="#fff" stroke-width="1.6" fill="none"/></svg>Funktionalität und Ästhetik</li>
    <li><svg width="12" height="12" viewBox="0 0 12 12"><circle cx="6" cy="6" r="6" fill="#f26722"/><path d="M3.2 6.2l2 2 3.6-4" stroke="#fff" stroke-width="1.6" fill="none"/></svg>Komplettlösungen mit rasche Umsetzung</li>
  </ul>

  <div class="pill benefits-pill">Ihre Vorteile</div>
  <ul class="benefits">
    <li><svg width="34" height="30" viewBox="0 0 34 30"><path d="M2 15h30l-3 9H5z" fill="#f7941d"/><path d="M8 15V6a4 4 0 0 1 8 0" stroke="#f7941d" stroke-width="2" fill="none"/></svg>Individuelle Badplanung</li>
    <li><svg width="34" height="30" viewBox="0 0 34 30"><circle cx="19" cy="17" r="10" stroke="#f7941d" stroke-width="2" fill="none"/><path d="M9 17h20M19 7v20" stroke="#f7941d" stroke-width="1.5"/><circle cx="9" cy="8" r="5" fill="#f7941d"/></svg>Eigene Handwerker vor Ort</li>
    <li><svg width="34" height="30" viewBox="0 0 34 30"><rect x="6" y="12" width="16" height="15" rx="2" stroke="#f7941d" stroke-width="2" fill="none"/><circle cx="24" cy="6" r="5" fill="#f7941d"/></svg>Traumbad erlebniss</li>
  </ul>

  <div class="footer">
    <svg class="footer-bg" width="761" height="65" viewBox="0 0 761 65">
      <defs><linearGradient id="footerBlue" x1="0" x2="1"><stop offset="0" stop-color="#1c8fd6"/><stop offset="1" stop-color="#0d5aa7"/></linearGradient></defs>
      <rect width="761" height="65" fill="url(#footerBlue)"/>
      <path d="M0 7H430L482 65H0Z" fill="#3a3a3c"/>
    </svg>
    <div class="contact web">
      <svg width="22" height="22" viewBox="0 0 22 22" fill="none" stroke="#f7941d" stroke-width="1.8"><circle cx="11" cy="11" r="9.5"/><ellipse cx="11" cy="11" rx="4.2" ry="9.5"/><path d="M1.5 11h19M3 6h16M3 16h16"/></svg>
      <span>www.wohnquell.at</span>
    </div>
    <div class="divider"></div>
    <div class="contact mail">
      <svg width="24" height="16" viewBox="0 0 24 16"><rect width="24" height="16" rx="1" fill="#f7941d"/><path d="M1 1l11 8 11-8" stroke="#3a3a3c" stroke-width="1.6" fill="none"/></svg>
      <span>office@wohnquell.at</span>
    </div>
    <div class="phone">
      <svg width="26" height="42" viewBox="0 0 26 42"><path d="M8 2c-4 1-6 4-6 9 0 9 5 22 13 28 3 2 6 1 8-1l-5-8-4 2c-3-4-5-11-5-16l4-1z" fill="#fff"/></svg>
      <span>0800 410 926</span>
    </div>
  </div>
</div>
</body>
</html>
```